drafting business needs a 2 sided rack card design. Size specificaton

Document Trim Size:
Full Bleed Size (starting document size)
3.86" x 8.39"
When trimmed the Rack cards are 3.74" x 8.27".
300 DPI

I need my logo, product info, and 2 pictures included

This is product information that i need:

- Floor Plans measured to KEDV & TRUZ standards
- Stunning HD Photography
- Vistaloom - your space delivered in perfect 3D
- E &O insured
- Our products delivered next by before 10:00 AM

It also has to my my special offer: Save 50% off Vistaloom, Floor Plans, and Photography

My contact info is
www.tidewellplans-demo.com
dorian@tidewellplans-demo.com
555-014-2286

Hey designers, the common element I see in most of the designs that I actually don't like is the use of orange and blue. I think there was some miscommunication. Please Don't use these colors. It really makes the designs Look cheap. I want a clean, high end look.

realtors

Real Estate

Serif

• At least 2 photos and my logo included. it must include all my wording with discount in bold, but classy.
• I want clean classy design. My logo is and 2 photos should be in design. I design should match my logo colors, I think. I have tons of other photos if you think these arent very useful
• Also I have attached a logo from vistaloom. Please include this, but smaller than the Tidewell Plans. The Vistaloom is just equiptment that I use
• This is a discount promotion, but I dont want it to look cheap whatsoever

```html
<!DOCTYPE html>
<html lang="en">
<head>
<meta charset="utf-8">
<title>Tidewell Plans Rack Cards</title>
<link href="https://fonts.googleapis.com/css2?family=Montserrat:wght@400;500;600;700;800&family=Oswald:wght@600&family=Libre+Baskerville&display=swap" rel="stylesheet">
<style>
  :root{
    --navy:#1f2a3a;
    --slate:#4a5566;
    --gold:#a8875a;
    --gold-soft:#cbb58f;
    --ink:#2a2a2a;
    --line:#b5b0a8;
    --bg:#e9e9e9;
    --paper:#ffffff;
  }
  *{box-sizing:border-box;margin:0;padding:0}
  html,body{width:1200px;height:942px;overflow:hidden;background:var(--bg);font-family:"Montserrat",sans-serif;color:var(--ink)}
  .rack-card{position:absolute;top:41px;width:389px;height:860px;background:var(--paper);overflow:hidden;box-shadow:0 6px 20px rgba(0,0,0,.15)}
  .rack-card--front{left:190px}
  .rack-card--back{left:621px}
  .shape{position:absolute;left:0;top:0}

  .brand{position:absolute;left:0;right:0;text-align:center}
  .brand__dot{width:72px;height:72px;border-radius:50%;background:var(--navy);margin:0 auto 10px}
  .brand__name{font-family:"Libre Baskerville",serif;font-size:27px;color:var(--navy);letter-spacing:.3px}

  .photo{position:absolute;left:0;right:0}
  .photo--bedroom{top:182px;height:238px;border-radius:0 60px 0 60px;background:linear-gradient(180deg,#d8cfc8 0%,#b9a9a4 45%,#d7cbd3 70%,#8f7f86 100%)}
  .photo--living{top:190px;height:236px;border-radius:0 0 0 60px;background:linear-gradient(160deg,#eef1f3 0%,#cfd6da 40%,#b9a38a 75%,#6e4d33 100%)}

  .headline{position:absolute;left:0;right:0;top:438px;text-align:center}
  .headline__main{font-size:32px;font-weight:800;color:var(--navy);line-height:1.05}
  .headline__sub{font-size:21px;font-weight:800;color:var(--gold);line-height:1.2}
  .headline__tag{font-size:14px;font-weight:700;color:var(--ink);margin-top:3px}

  .product-info{position:absolute;left:22px;right:22px;top:540px;height:188px;border:1.5px solid var(--line);border-radius:18px;padding:28px 14px 0 14px}
  .product-info__title{position:absolute;top:-11px;left:50%;transform:translateX(-50%);background:var(--paper);padding:0 8px;font-size:15px;font-weight:800;color:var(--navy);white-space:nowrap}
  .product-info__list{list-style:none}
  .product-info__item{display:flex;align-items:center;gap:8px;font-size:11.5px;font-weight:500;margin-bottom:12px}
  .tick{flex:none;width:16px;height:16px}

  .equipment{position:absolute;left:0;right:0;top:738px;display:flex;justify-content:center;align-items:center;gap:6px;font-size:11px;font-weight:600;color:var(--slate);letter-spacing:1px}
  .equipment__mark{width:9px;height:9px;background:var(--slate)}

  .call-band__phone{position:absolute;top:790px;left:0;right:0;text-align:center;color:#fff;font-weight:700;font-size:18px}
  .site{position:absolute;left:0;right:0;text-align:center;color:#fff;font-size:12px;letter-spacing:3px;font-weight:500}
  .site--front{top:830px}
  .site--back{top:826px}

  .offer{position:absolute;left:38px;right:38px;top:478px;height:148px;border:1.5px solid var(--line);border-radius:18px;box-shadow:0 3px 8px rgba(0,0,0,.15);background:var(--paper)}
  .offer__ribbon{position:absolute;left:-26px;top:-14px;background:var(--gold);color:#fff;font-weight:700;font-size:15px;padding:7px 18px;letter-spacing:.5px}
  .offer__save{position:absolute;left:28px;top:34px;width:20px;height:54px;background:var(--navy);color:#fff;font-size:11px;font-weight:700;writing-mode:vertical-rl;transform:rotate(180deg);text-align:center;line-height:20px}
  .offer__amount{position:absolute;left:54px;top:24px;font-family:"Oswald",sans-serif;font-weight:600;font-size:64px;line-height:1;color:var(--navy)}
  .offer__what{position:absolute;left:0;right:0;top:98px;text-align:center;font-size:16px;line-height:1.15}
  .offer__what strong{font-weight:800;text-transform:uppercase}

  .contact{position:absolute;left:0;right:0;top:662px;text-align:center}
  .contact__lead{font-size:16px;font-weight:700;color:var(--gold)}
  .contact__phone{font-size:23px;font-weight:700;margin-top:4px;display:flex;justify-content:center;align-items:center;gap:6px;color:var(--navy)}
  .contact__mail{font-size:13px;margin-top:3px;display:flex;justify-content:center;align-items:center;gap:6px}
  .icon{width:16px;height:16px}
</style>
</head>
<body>

<section class="rack-card rack-card--front">
  <div class="brand" style="top:32px">
    <div class="brand__dot"></div>
    <div class="brand__name">Tidewell Plans</div>
  </div>
  <svg class="shape" width="389" height="860" aria-hidden="true">
    <path d="M0 176 L300 158 Q318 157 330 162" stroke="var(--gold)" stroke-width="4" fill="none"/>
  </svg>
  <div class="photo photo--bedroom" role="img" aria-label="Photo of a staged bedroom with a tufted bed, bedside lamps and a round mirror"></div>
  <svg class="shape" width="389" height="860" aria-hidden="true">
    <path d="M60 432 Q80 424 120 424 L389 412" stroke="var(--navy)" stroke-width="4" fill="none"/>
    <rect x="0" y="770" width="389" height="90" fill="var(--navy)"/>
    <rect x="0" y="818" width="389" height="42" fill="var(--gold)"/>
  </svg>
  <div class="headline">
    <div class="headline__main">FLOOR PLANS</div>
    <div class="headline__sub">PROPERTY PHOTOGRAPHY</div>
    <div class="headline__tag">Vistaloom: Real Spaces in Perfect 3D</div>
  </div>
  <div class="product-info">
    <div class="product-info__title">PRODUCT INFORMATION</div>
    <ul class="product-info__list">
      <li class="product-info__item"><svg class="tick" viewBox="0 0 16 16"><circle cx="8" cy="8" r="7.5" fill="var(--slate)"/><path d="M4.5 8.2l2.3 2.3 4.7-4.8" stroke="#fff" stroke-width="1.6" fill="none"/></svg>Floor Plans measured to KEDV &amp; TRUZ standards</li>
      <li class="product-info__item"><svg class="tick" viewBox="0 0 16 16"><circle cx="8" cy="8" r="7.5" fill="var(--slate)"/><path d="M4.5 8.2l2.3 2.3 4.7-4.8" stroke="#fff" stroke-width="1.6" fill="none"/></svg>Stunning HD Photography</li>
      <li class="product-info__item"><svg class="tick" viewBox="0 0 16 16"><circle cx="8" cy="8" r="7.5" fill="var(--slate)"/><path d="M4.5 8.2l2.3 2.3 4.7-4.8" stroke="#fff" stroke-width="1.6" fill="none"/></svg>Vistaloom - your space delivered in perfect 3D</li>
      <li class="product-info__item"><svg class="tick" viewBox="0 0 16 16"><circle cx="8" cy="8" r="7.5" fill="var(--slate)"/><path d="M4.5 8.2l2.3 2.3 4.7-4.8" stroke="#fff" stroke-width="1.6" fill="none"/></svg>E &amp;O insured</li>
      <li class="product-info__item"><svg class="tick" viewBox="0 0 16 16"><circle cx="8" cy="8" r="7.5" fill="var(--slate)"/><path d="M4.5 8.2l2.3 2.3 4.7-4.8" stroke="#fff" stroke-width="1.6" fill="none"/></svg>Our products delivered next by before 10:00 AM</li>
    </ul>
  </div>
  <div class="equipment"><span class="equipment__mark"></span>Vistaloom</div>
  <div class="call-band__phone">Call Us &#9742; 555-014-2286</div>
  <div class="site site--front">WWW.TIDEWELLPLANS-DEMO.COM</div>
</section>

<section class="rack-card rack-card--back">
  <svg class="shape" width="389" height="860" aria-hidden="true">
    <rect x="0" y="0" width="389" height="5" fill="var(--gold)"/>
    <rect x="0" y="0" width="5" height="300" fill="var(--gold)"/>
    <rect x="12" y="12" width="377" height="1.5" fill="var(--gold)"/>
    <rect x="12" y="12" width="1.5" height="290" fill="var(--gold)"/>
  </svg>
  <div class="brand" style="top:52px">
    <div class="brand__dot"></div>
    <div class="brand__name">Tidewell Plans</div>
  </div>
  <div class="photo photo--living" role="img" aria-label="Photo of a bright living room with large windows, fireplace and a patterned rug"></div>
  <svg class="shape" width="389" height="860" aria-hidden="true">
    <path d="M60 438 Q80 430 120 430 L389 420" stroke="var(--navy)" stroke-width="4" fill="none"/>
    <path d="M40 790 L389 780" stroke="var(--navy)" stroke-width="3" fill="none"/>
    <path d="M0 808 L389 790 L389 860 L0 860 Z" fill="var(--navy)"/>
  </svg>
  <div class="offer">
    <div class="offer__ribbon">SPECIAL OFFER:</div>
    <div class="offer__save">SAVE</div>
    <div class="offer__amount">50% OFF</div>
    <div class="offer__what">Vistaloom, Floor Plans,<br><strong>and Photography</strong></div>
  </div>
  <div class="contact">
    <div class="contact__lead">For more details Contact Us</div>
    <div class="contact__phone"><svg class="icon" viewBox="0 0 16 16"><path d="M3 1.5l3 .5 1 3-1.6 1.3a8 8 0 0 0 4.3 4.3L11 9l3 1 .5 3-2 1.5C7 14 2 9 1.5 3.5Z" fill="var(--navy)"/></svg>555-014-2286</div>
    <div class="contact__mail"><svg class="icon" viewBox="0 0 16 16"><rect x="1" y="3.5" width="14" height="9" rx="1" fill="none" stroke="var(--navy)" stroke-width="1.4"/><path d="M1.5 4l6.5 5 6.5-5" fill="none" stroke="var(--navy)" stroke-width="1.4"/></svg>dorian@tidewellplans-demo.com</div>
  </div>
  <div class="site site--back">WWW.TIDEWELLPLANS-DEMO.COM</div>
</section>

</body>
</html>
```